依頼詳細
インターネット通販の本格的な正統派バレエショップ(ヨーロッパ風)を目指していますので、それに合うデザインと同時に、色のレギュレーションなどを決めてプロっぽいホームページを作りたいと思っています。
現在のホームページは色々な色があり、色のレギュレーションが出来ていませんので、今回のリニューアルと同時にメインカラー、ザブカラー、アクセントカラーなどを決めてプロっぽいページ作成をする為に依頼をしました。

既にロゴは決めているので、添付したロゴの色とイメージに合わせて作って下さい。

サイトURL
www.kolvimeta.com
ページ数
1ページ
希望イメージ
シンプル 複雑
単色 カラフル
暗い 明るい
日常 高級
遊び心 厳粛
未来的 伝統的
女性的 男性的
希望する色
紫系、白のベースカラーにロゴ色である藤色をサブカラーと考えています。
納品ファイル
• イラストレーター形式 (.ai)
• フォトショップ形式 (.psd)
補足説明
ロゴを添付しました。
上部分の看板についてですが、添付しました看板を参考にお願いします。
現在のページですと看板が高く下にスクロールをしないと情報が見れないので、
直にわかるように看板を縦に短くしたいです。

報告が遅くなり大変申し訳ございませんでした。
■ 選んだ理由

ターゲットの年齢層にマッチしたデザインと、色使いがとても気に入りました。

■ 提案者全員のお礼・コメント

沢山の方がデザインをして下さり大変嬉しく思います。本当にありがとうございました。

```html
<!DOCTYPE html>
<html lang="ja">
<head>
<meta charset="utf-8">
<title>Kolvimeta バレエ用品専門店</title>
<link href="https://fonts.googleapis.com/css2?family=Noto+Sans+JP:wght@400;700&family=Cormorant+Garamond:wght@600&display=swap" rel="stylesheet">
<style>
:root{
  --lilac:#9b94c7;
  --lilac-dark:#6d64a8;
  --lilac-deep:#4f4788;
  --lilac-soft:#e7e4f3;
  --lilac-pale:#f4f2fa;
  --line:#cfcae6;
  --ink:#4a4560;
  --muted:#8a86a0;
  --pink:#e07aa6;
  --gold:#c9a84a;
  --white:#ffffff;
  --photo-a:#ede7f2;
  --photo-b:#d9cfe6;
}
*{box-sizing:border-box;margin:0;padding:0}
html,body{width:1200px;height:2732px;overflow:hidden}
body{background:var(--white);font-family:"Noto Sans JP",sans-serif;color:var(--ink);font-size:13px;position:relative}
.serif{font-family:"Cormorant Garamond",serif}
.photo{background:linear-gradient(160deg,var(--photo-a),var(--photo-b))}

/* header */
.site-header{position:absolute;left:0;top:0;width:1200px;height:68px;background:linear-gradient(#fff,var(--lilac-pale));border-bottom:1px solid var(--line)}
.tagline{position:absolute;left:18px;top:6px;font-size:11px;color:var(--muted)}
.brand{position:absolute;left:18px;top:18px;display:flex;align-items:center;gap:10px}
.brand-mark{width:34px;height:34px;border-radius:50%;background:var(--lilac)}
.brand-name{font-family:"Cormorant Garamond",serif;font-size:40px;color:var(--lilac-dark);line-height:1}
.brand-sub{position:absolute;left:230px;top:40px;font-size:11px;color:var(--lilac-dark)}
.contact{position:absolute;right:18px;top:6px;width:330px;height:56px}
.contact-note{font-size:10px;color:#fff;background:var(--lilac);border-radius:3px;padding:2px 8px;display:inline-block;position:absolute;right:0;top:0}
.contact-tel{position:absolute;left:0;top:20px;display:flex;align-items:center;gap:6px;font-size:24px;font-weight:700;color:var(--lilac-deep)}
.contact-sub{position:absolute;left:36px;top:46px;font-size:10px;color:var(--muted)}

/* nav */
.global-nav{position:absolute;left:0;top:68px;width:1200px;height:40px;background:linear-gradient(var(--lilac-soft),#d4cfea);display:flex;padding:0 12px;border-bottom:1px solid var(--line)}
.global-nav a{flex:1;text-align:center;line-height:40px;font-size:13px;color:var(--lilac-deep);text-decoration:none;border-right:1px solid #fff}
.global-nav a:first-child{border-left:1px solid #fff}

/* category row */
.category-grid{position:absolute;left:12px;top:116px;width:1176px;height:160px;display:grid;grid-template-columns:repeat(9,1fr);gap:6px 8px;padding:8px;background:var(--lilac-pale);border:1px solid var(--line)}
.category{display:flex;align-items:center;gap:6px;background:#fff;border:1px solid var(--line);padding:4px}
.category .thumb{width:56px;height:56px;flex:none}
.category span{font-size:11px;color:var(--lilac-deep);line-height:1.3}

/* sidebar */
.sidebar{position:absolute;left:12px;top:288px;width:184px}
.side-box{border:1px solid var(--line);margin-bottom:12px;background:#fff}
.side-head{background:var(--lilac);color:#fff;font-family:"Cormorant Garamond",serif;font-size:16px;padding:3px 8px;letter-spacing:1px}
.side-head small{font-family:"Noto Sans JP",sans-serif;font-size:10px;margin-left:4px}
.side-body{padding:8px;font-size:11px}
.field{height:20px;border:1px solid var(--line);margin:3px 0 6px;background:#fff}
.btn{display:block;margin:4px auto;width:80px;height:22px;border-radius:3px;background:var(--lilac-dark);color:#fff;text-align:center;line-height:22px;font-size:11px}
.link-list li{list-style:none;font-size:11px;color:var(--lilac-deep);padding:2px 0}
.swatches{display:grid;grid-template-columns:repeat(6,1fr);gap:5px;margin:6px 0}
.swatches i{display:block;height:18px;border-radius:50%;border:1px solid var(--line)}
.banner{border:1px solid var(--line);margin-bottom:10px;padding:10px;text-align:center;color:var(--lilac-deep);background:linear-gradient(#fff,var(--lilac-pale))}
.banner b{display:block;font-size:16px}
.banner span{font-size:10px;color:var(--muted)}
.banner.tall{height:120px}
.banner .pic{height:56px;margin-top:6px}

/* main */
.main{position:absolute;left:208px;top:288px;width:980px}
.hero{position:relative;height:310px;border:1px solid var(--line);overflow:hidden}
.hero-photo{position:absolute;inset:0}
.hero-title{position:absolute;left:260px;top:24px;font-size:30px;font-weight:700;color:var(--lilac-deep)}
.hero-copy{position:absolute;left:260px;top:72px;width:420px;font-size:12px;line-height:1.8}
.badges{position:absolute;left:250px;top:150px;display:flex;gap:14px}
.badge{width:96px;height:96px;border-radius:50%;background:var(--lilac-dark);color:#fff;display:flex;align-items:center;justify-content:center;text-align:center;font-size:13px;font-weight:700;line-height:1.4}
.hero-girl{position:absolute;left:0;top:0;width:230px;height:310px}
.hero-side{position:absolute;right:0;top:0;width:260px;height:310px}
.notice{height:44px;background:var(--lilac-dark);color:#fff;font-size:13px;display:flex;flex-direction:column;justify-content:center;padding:0 18px;line-height:1.5}

.section-head{display:flex;align-items:baseline;gap:8px;border-bottom:2px solid var(--lilac);padding:4px 6px;margin-top:14px;background:var(--lilac-pale)}
.section-head h2{font-family:"Cormorant Garamond",serif;font-size:22px;color:var(--lilac-deep);font-weight:600;letter-spacing:1px}
.section-head span{font-size:11px;color:var(--muted)}
.news{padding:6px 10px}
.news li{list-style:none;font-size:12px;line-height:1.75;border-bottom:1px dotted var(--line)}
.news time{color:var(--lilac-dark);margin-right:12px}

.pickup{display:grid;grid-template-columns:repeat(6,1fr);gap:10px;padding:10px}
.item .pic{height:170px;border:1px solid var(--line)}
.item p{font-size:10px;line-height:1.4;margin-top:4px}
.item em{font-style:normal;color:var(--pink);font-weight:700;font-size:11px}

.ranking{border:1px solid var(--line);margin-top:10px;padding:8px}
.rank-title{display:flex;align-items:center;gap:8px;font-size:15px;font-weight:700;color:var(--lilac-deep);border-bottom:1px dashed var(--line);padding-bottom:6px}
.rank-grid{display:grid;grid-template-columns:repeat(7,1fr);gap:8px;padding-top:8px}
.rank-grid .pic{height:118px;border:1px solid var(--line);position:relative}
.rank-no{position:absolute;left:0;top:0;background:var(--lilac-dark);color:#fff;font-size:10px;padding:1px 5px}
.rank-grid p{font-size:10px;line-height:1.4;margin-top:3px}

.topics{display:grid;grid-template-columns:1fr 1fr;gap:16px;margin-top:10px}
.feed{border:1px solid var(--line);padding:10px}
.feed-head{font-size:13px;font-weight:700;color:var(--lilac-deep);border-bottom:1px solid var(--line);padding-bottom:6px;display:flex;align-items:center;gap:6px}
.feed-head i{width:14px;height:14px;background:var(--lilac);display:inline-block}
.post{display:flex;gap:8px;padding:8px 0;border-bottom:1px dotted var(--line)}
.post .av{width:36px;height:36px;flex:none;background:var(--lilac-soft)}
.post div p{font-size:11px;line-height:1.5}
.post .who{color:var(--lilac-dark);font-weight:700}
.post .pic{height:70px;width:110px;margin-top:4px}
.fans{display:grid;grid-template-columns:repeat(8,1fr);gap:4px;margin-top:8px}
.fans i{height:44px;background:var(--lilac-soft);display:block}

/* footer */
.site-footer{position:absolute;left:0;top:2412px;width:1200px;height:320px}
.footer-band{height:190px;background:var(--lilac);color:#fff;display:flex;padding:24px 40px;gap:40px}
.footer-brand{width:180px;height:120px;background:var(--lilac-dark);display:flex;flex-direction:column;align-items:center;justify-content:center;gap:6px}
.footer-brand .brand-name{color:#fff;font-size:30px}
.footer-info{flex:1;font-size:13px;line-height:1.9}
.footer-info b{font-size:15px}
.footer-points{width:460px;font-size:13px;line-height:1.9;background:var(--lilac-dark);padding:14px 18px}
.footer-nav{height:40px;background:var(--lilac-soft);display:flex;justify-content:center;gap:26px;line-height:40px;font-size:12px;color:var(--lilac-deep)}
.copyright{text-align:center;font-size:11px;color:var(--muted);padding-top:26px}
</style>
</head>
<body>

<header class="site-header">
  <p class="tagline">バレエの先生もオススメする、お子様指導の正統派バレエショップ</p>
  <div class="brand"><span class="brand-mark"></span><span class="brand-name">Kolvimeta</span></div>
  <p class="brand-sub">バレエ用品専門店</p>
  <div class="contact">
    <span class="contact-note">バレエ用品のネットショップはお任せ</span>
    <div class="contact-tel">
      <svg width="28" height="24" viewBox="0 0 28 24"><path d="M6 3c2-1 4 0 5 2l1 3c0 1-1 2-2 3 1 3 4 6 7 7 1-1 2-2 3-2l3 1c2 1 3 3 2 5-1 2-3 3-6 2C11 22 4 15 3 8 2 5 4 4 6 3z" fill="var(--lilac-dark)"/></svg>
      0120-482-915
    </div>
    <p class="contact-sub">携帯電話はこちら 03-5521-7740</p>
  </div>
</header>

<nav class="global-nav">
  <a>トップページ</a><a>店舗紹介</a><a>お支払い方法</a><a>定額発送サービス</a><a>ラッピング</a><a>メールマガジン</a><a>お問合せ</a><a>カート</a>
</nav>

<section class="category-grid">
  <div class="category"><div class="thumb photo" role="img" aria-label="子供レオタード"></div><span>子供<br>レオタード</span></div>
  <div class="category"><div class="thumb photo" role="img" aria-label="チュチュレオタード"></div><span>チュチュ<br>レオタード</span></div>
  <div class="category"><div class="thumb photo" role="img" aria-label="大人レオタード"></div><span>Jr.&amp;大人<br>レオタード</span></div>
  <div class="category"><div class="thumb photo" role="img" aria-label="スカート"></div><span>バレエ<br>スカート</span></div>
  <div class="category"><div class="thumb photo" role="img" aria-label="タイツ"></div><span>バレエ<br>タイツ</span></div>
  <div class="category"><div class="thumb photo" role="img" aria-label="シューズ"></div><span>バレエ<br>シューズ</span></div>
  <div class="category"><div class="thumb photo" role="img" aria-label="トウシューズ"></div><span>トウ<br>シューズ</span></div>
  <div class="category"><div class="thumb photo" role="img" aria-label="ウォームアップ"></div><span>ウォーム<br>アップ</span></div>
  <div class="category"><div class="thumb photo" role="img" aria-label="バッグ"></div><span>バレエ<br>バッグ</span></div>
  <div class="category"><div class="thumb photo" role="img" aria-label="髪飾り"></div><span>髪飾り<br>アクセサリー</span></div>
  <div class="category"><div class="thumb photo" role="img" aria-label="ストレッチ用品"></div><span>ストレッチ<br>用品</span></div>
  <div class="category"><div class="thumb photo" role="img" aria-label="男性用品"></div><span>男性<br>バレエ用品</span></div>
  <div class="category"><div class="thumb photo" role="img" aria-label="ケア用品"></div><span>トウ<br>ケア用品</span></div>
  <div class="category"><div class="thumb photo" role="img" aria-label="DVDと本"></div><span>DVD<br>書籍</span></div>
  <div class="category"><div class="thumb photo" role="img" aria-label="雑貨"></div><span>バレエ<br>雑貨</span></div>
  <div class="category"><div class="thumb photo" role="img" aria-label="ギフト"></div><span>発表会<br>ギフト</span></div>
  <div class="category"><div class="thumb photo" role="img" aria-label="セール品"></div><span>アウト<br>レット</span></div>
  <div class="category"><div class="thumb photo" role="img" aria-label="新着商品"></div><span>新着<br>アイテム</span></div>
</section>

<aside class="sidebar">
  <div class="side-box">
    <div class="side-head">LOGIN<small>ログイン</small></div>
    <div class="side-body">
      <p>メールアドレス</p><div class="field"></div>
      <p>パスワード</p><div class="field"></div>
      <span class="btn">ログイン</span>
      <ul class="link-list"><li>› 新規会員登録はこちら</li><li>› パスワードを忘れた方</li></ul>
    </div>
  </div>
  <div class="side-box">
    <div class="side-head">SEARCH<small>商品検索</small></div>
    <div class="side-body">
      <div class="field"></div>
      <span class="btn">検索</span>
      <p>カラーから探す</p>
      <div class="swatches">
        <i style="background:#fff"></i><i style="background:#111"></i><i style="background:#f2b6c8"></i><i style="background:#d83b5e"></i><i style="background:#9b94c7"></i><i style="background:#6a5aa8"></i>
        <i style="background:#8cc4e6"></i><i style="background:#2d4f9a"></i><i style="background:#8fcf9a"></i><i style="background:#f3dc7a"></i><i style="background:#f2a560"></i><i style="background:#999"></i>
      </div>
      <ul class="link-list"><li>› サイズから探す</li><li>› 価格から探す</li><li>› ブランドから探す</li></ul>
    </div>
  </div>
  <div class="side-box">
    <div class="side-head">MAGAZINE<small>メルマガ</small></div>
    <div class="side-body">
      <p>新商品やセール情報をいち早くお届けします。</p>
      <div class="field"></div>
      <span class="btn">登録する</span>
    </div>
  </div>
  <div class="banner tall"><span>気になるあれこれ</span><b>バレエQ&amp;A</b><div class="pic photo" role="img" aria-label="バレエQ&amp;Aのイメージ写真"></div></div>
  <div class="banner tall"><span>はじめての方へ</span><b>バレエ用品の選び方</b><div class="pic photo" role="img" aria-label="バレエ用品の写真"></div></div>
  <div class="banner"><b>よくあるご質問</b><span>FAQ</span></div>
  <div class="banner tall"><span>VOICE</span><b>お客様の声</b><div class="pic photo" role="img" aria-label="お客様の声の写真"></div></div>
  <div class="banner"><span>商品をお持ちの方へ</span><b>レビュー募集中</b></div>
  <div class="banner"><b>無料ラッピング</b><span>承ります</span></div>
  <div class="banner tall"><span>まとめて買うと</span><b>お買い得セット</b><div class="pic photo" role="img" aria-label="セット商品の写真"></div></div>
  <div class="banner"><span>先生方へ</span><b>バレエ教室支援</b></div>
  <div class="banner tall"><span>一緒に働きませんか</span><b>スタッフ募集中</b><div class="pic photo" role="img" aria-label="スタッフ募集のイメージ"></div></div>
  <div class="banner"><b>店舗のご案内</b><span>アクセス・営業時間</span></div>
</aside>

<main class="main">
  <section class="hero">
    <div class="hero-photo photo" style="background:linear-gradient(120deg,#f6f3fb,#e4dff1)"></div>
    <div class="hero-girl photo" role="img" aria-label="レオタード姿で踊るバレリーナの写真"></div>
    <div class="hero-side photo" role="img" aria-label="トウシューズとチュチュの写真"></div>
    <h1 class="hero-title">コルヴィメタへようこそ！</h1>
    <p class="hero-copy">お客様の安心してお買い物をしていただけるよう、すべての商品を丁寧にお届けします。レッスン用品から発表会まで幅広くご用意しております。</p>
    <div class="badges">
      <div class="badge">5,000円以上<br>送料無料</div>
      <div class="badge">ポイント<br>使用保証</div>
      <div class="badge">返品交換<br>保証</div>
    </div>
  </section>
  <div class="notice">
    <p>期間限定！ただいま5,000円以上のお買い上げで送料無料キャンペーン実施中です。</p>
    <p>ご注文の際は定額発送サービスもぜひご利用ください。</p>
  </div>

  <div class="section-head"><h2>NEWS</h2><span>新着情報</span></div>
  <ul class="news">
    <li><time>7月17日</time>新商品【子供用】シフォンスカートを販売開始しました！</li>
    <li><time>7月10日</time>新商品【大人用】キャミソールレオタードを販売開始しました！</li>
    <li><time>7月3日</time>新商品【子供用】チュチュレオタードを販売開始しました！</li>
    <li><time>6月18日</time>夏季休業日のお知らせを掲載しました。</li>
  </ul>

  <div class="section-head"><h2>PICKUP</h2><span>おすすめ商品</span></div>
  <div class="pickup">
    <div class="item"><div class="pic photo" role="img" aria-label="ピンクのレオタード"></div><p>キャミソールレオタード<br><em>¥3,980</em></p></div>
    <div class="item"><div class="pic photo" role="img" aria-label="白のレオタード"></div><p>フレンチ袖レオタード<br><em>¥4,200</em></p></div>
    <div class="item"><div class="pic photo" role="img" aria-label="スカート付きレオタード"></div><p>スカート付きレオタード<br><em>¥4,800</em></p></div>
    <div class="item"><div class="pic photo" role="img" aria-label="黒のレオタード"></div><p>ベーシックレオタード<br><em>¥3,600</em></p></div>
    <div class="item"><div class="pic photo" role="img" aria-label="巻きスカート"></div><p>シフォン巻きスカート<br><em>¥2,400</em></p></div>
    <div class="item"><div class="pic photo" role="img" aria-label="トウシューズ"></div><p>トウシューズ定番型<br><em>¥9,800</em></p></div>
  </div>

  <div class="section-head"><h2>RANKING</h2><span>人気ランキング</span></div>

  <div class="ranking">
    <div class="rank-title"><svg width="22" height="16" viewBox="0 0 22 16"><path d="M1 4l5 5 5-8 5 8 5-5-2 11H3z" fill="var(--gold)"/></svg>子供レオタード部門</div>
    <div class="rank-grid">
      <div><div class="pic photo" role="img" aria-label="子供レオタード1位"><span class="rank-no">1位</span></div><p>半袖レオタード<br>¥3,200</p></div>
      <div><div class="pic photo" role="img" aria-label="子供レオタード2位"><span class="rank-no">2位</span></div><p>キャミレオタード<br>¥2,980</p></div>
      <div><div class="pic photo" role="img" aria-label="子供レオタード3位"><span class="rank-no">3位</span></div><p>スカート付き<br>¥3,800</p></div>
      <div><div class="pic photo" role="img" aria-label="子供レオタード4位"><span class="rank-no">4位</span></div><p>長袖レオタード<br>¥3,500</p></div>
      <div><div class="pic photo" role="img" aria-label="子供レオタード5位"><span class="rank-no">5位</span></div><p>フリル袖タイプ<br>¥3,400</p></div>
      <div><div class="pic photo" role="img" aria-label="子供レオタード6位"><span class="rank-no">6位</span></div><p>ベーシック型<br>¥2,800</p></div>
      <div><div class="pic photo" role="img" aria-label="子供レオタード7位"><span class="rank-no">7位</span></div><p>リボン付き<br>¥3,600</p></div>
    </div>
  </div>

  <div class="ranking">
    <div class="rank-title"><svg width="22" height="16" viewBox="0 0 22 16"><path d="M1 4l5 5 5-8 5 8 5-5-2 11H3z" fill="var(--gold)"/></svg>チュチュレオタード部門</div>
    <div class="rank-grid">
      <div><div class="pic photo" role="img" aria-label="チュチュレオタード1位"><span class="rank-no">1位</span></div><p>ピンクチュチュ<br>¥4,800</p></div>
      <div><div class="pic photo" role="img" aria-label="チュチュレオタード2位"><span class="rank-no">2位</span></div><p>ホワイトチュチュ<br>¥4,800</p></div>
      <div><div class="pic photo" role="img" aria-label="チュチュレオタード3位"><span class="rank-no">3位</span></div><p>花飾りチュチュ<br>¥5,200</p></div>
      <div><div class="pic photo" role="img" aria-label="チュチュレオタード4位"><span class="rank-no">4位</span></div><p>パープルチュチュ<br>¥4,600</p></div>
      <div><div class="pic photo" role="img" aria-label="チュチュレオタード5位"><span class="rank-no">5位</span></div><p>二段チュチュ<br>¥5,400</p></div>
      <div><div class="pic photo" role="img" aria-label="チュチュレオタード6位"><span class="rank-no">6位</span></div><p>ラメ入りチュチュ<br>¥5,600</p></div>
      <div><div class="pic photo" role="img" aria-label="チュチュレオタード7位"><span class="rank-no">7位</span></div><p>水色チュチュ<br>¥4,600</p></div>
    </div>
  </div>

  <div class="ranking">
    <div class="rank-title"><svg width="22" height="16" viewBox="0 0 22 16"><path d="M1 4l5 5 5-8 5 8 5-5-2 11H3z" fill="var(--gold)"/></svg>Jr.&amp;大人レオタード部門</div>
    <div class="rank-grid">
      <div><div class="pic photo" role="img" aria-label="大人レオタード1位"><span class="rank-no">1位</span></div><p>ブラックキャミ<br>¥5,800</p></div>
      <div><div class="pic photo" role="img" aria-label="大人レオタード2位"><span class="rank-no">2位</span></div><p>ネイビー半袖<br>¥5,600</p></div>
      <div><div class="pic photo" role="img" aria-label="大人レオタード3位"><span class="rank-no">3位</span></div><p>バックレース<br>¥6,400</p></div>
      <div><div class="pic photo" role="img" aria-label="大人レオタード4位"><span class="rank-no">4位</span></div><p>ワインカラー<br>¥5,900</p></div>
      <div><div class="pic photo" role="img" aria-label="大人レオタード5位"><span class="rank-no">5位</span></div><p>長袖ベーシック<br>¥6,200</p></div>
      <div><div class="pic photo" role="img" aria-label="大人レオタード6位"><span class="rank-no">6位</span></div><p>メッシュ切替<br>¥6,800</p></div>
      <div><div class="pic photo" role="img" aria-label="大人レオタード7位"><span class="rank-no">7位</span></div><p>スカート付き<br>¥6,600</p></div>
    </div>
  </div>

  <div class="section-head"><h2>TOPICS</h2><span>スタッフブログ・お知らせ</span></div>
  <div class="topics">
    <div class="feed">
      <div class="feed-head"><i></i>Friendboard</div>
      <div class="post"><div class="av"></div><div><p class="who">コルヴィメタ</p><p>発表会シーズンに向けて新作チュチュが入荷しました。</p><div class="pic photo" role="img" aria-label="新作チュチュの写真"></div></div></div>
      <div class="post"><div class="av"></div><div><p class="who">コルヴィメタ</p><p>夏季休業日のお知らせです。ご注文は通常通り受付します。</p></div></div>
      <div class="post"><div class="av"></div><div><p class="who">コルヴィメタ</p><p>お客様から素敵なお写真をいただきました。ありがとうございます。</p><div class="pic photo" role="img" aria-label="レッスン風景の写真"></div></div></div>
      <div class="post"><div class="av"></div><div><p class="who">コルヴィメタ</p><p>スタッフおすすめのトウシューズケアをご紹介します。</p></div></div>
      <p style="font-size:11px;margin-top:8px">1,240人が「いいね！」と言っています</p>
      <div class="fans">
        <i role="img" aria-label="ファンのアイコン"></i><i></i><i></i><i></i><i></i><i></i><i></i><i></i>
        <i></i><i></i><i></i><i></i><i></i><i></i><i></i><i></i>
      </div>
    </div>
    <div class="feed">
      <div class="feed-head"><i></i>Chirpline <span style="font-weight:400;font-size:11px;color:var(--muted)">@kolvimeta</span></div>
      <div class="post"><div class="av"></div><div><p class="who">コルヴィメタ</p><p>新作スカートの撮影をしています。近日公開予定です。</p></div></div>
      <div class="post"><div class="av"></div><div><p class="who">コルヴィメタ</p><p>本日15時までのご注文は当日発送いたします。</p></div></div>
      <div class="post"><div class="av"></div><div><p class="who">コルヴィメタ</p><p>送料無料キャンペーンは今月末までです。お見逃しなく。</p></div></div>
      <div class="post"><div class="av"></div><div><p class="who">コルヴィメタ</p><p>人気のキャミレオタードが再入荷しました。</p></div></div>
      <div class="post"><div class="av"></div><div><p class="who">コルヴィメタ</p><p>レビュー投稿でポイントをプレゼント中です。</p></div></div>
      <div class="post"><div class="av"></div><div><p class="who">コルヴィメタ</p><p>スタッフブログを更新しました。ぜひご覧ください。</p></div></div>
      <div class="post"><div class="av"></div><div><p class="who">コルヴィメタ</p><p>ラッピング用の新しいリボンが届きました。</p></div></div>
      <div class="post"><div class="av"></div><div><p class="who">コルヴィメタ</p><p>明日は定休日です。メールは翌営業日に返信します。</p></div></div>
    </div>
  </div>
</main>

<footer class="site-footer">
  <div class="footer-band">
    <div class="footer-brand"><span class="brand-name">Kolvimeta</span><span style="font-size:11px">www.kolvimeta.com</span></div>
    <div class="footer-info">
      <p>バレエの先生もオススメする、お子様指導の正統派バレエショップ</p>
      <p><b>定休日：日曜日・祝日</b></p>
      <p>営業時間：平日9:00〜18:00</p>
      <p>TEL 0120-482-915</p>
    </div>
    <div class="footer-points">
      <p>・送料・手数料 5,000円以上のお買い上げで送料無料</p>
      <p>・銀行振込手数料はお客様負担となります</p>
      <p>・返品交換は商品到着後7日以内に承ります</p>
    </div>
  </div>
  <nav class="footer-nav"><span>トップページ</span><span>店舗紹介</span><span>お支払い方法</span><span>定額発送サービス</span><span>ラッピング</span><span>メールマガジン</span><span>お問合せ</span><span>個人情報の取扱い</span></nav>
  <p class="copyright">Copyright © Kolvimeta All Rights Reserved.</p>
</footer>

</body>
</html>
```